Mezzanine Floor Manufacturer looking for a new business card design

We manufacture mezzanine floors and are providers of racking systems. We provide a range of items/services - simple rack repairs , full warehouse fit outs , manufacturer and install mezzanine floors , partitioning and large turnkey projects. Recently had a new website - www.corvane-shelving.co.uk and would like our business cards updating aswell . Our current card is single sided in the old logo colours (pdf attached) and needs updating.

Target Market(s)

We deal with large projects/ multi national companies and also smaller projects and companies throughout the UK ranging from a single warehouse to a large multi site company.

Industry/Entity Type

Business

Contact Information for Business Card

Will have job title,tel no's, email ,website address etc like example pdf

Requirements
Must have
• Hi - needs to use the colours of the logo & new website. Card needs to be professional

```html
<!DOCTYPE html>
<html lang="en">
<head>
<meta charset="utf-8">
<title>Corvane Shelving – Business Card</title>
<link rel="stylesheet" href="https://fonts.googleapis.com/css2?family=Barlow+Condensed:wght@500;600&display=swap">
<style>
  :root {
    --brand-red: #c8202f;
    --ink: #1e1e20;
    --card: #f6f6f7;
    --backdrop: #2b2b2c;
  }
  * { margin: 0; padding: 0; box-sizing: border-box; }
  html, body { width: 1200px; height: 800px; overflow: hidden; background: var(--backdrop); }
  body {
    font-family: "Barlow Condensed", "Arial Narrow", sans-serif;
    color: var(--ink);
    display: flex;
    align-items: center;
    justify-content: center;
    gap: 40px;
  }
  .card {
    position: relative;
    width: 540px;
    height: 336px;
    background: var(--card);
    border-radius: 4px;
    overflow: hidden;
  }

  /* Contact side */
  .card__rule {
    position: absolute;
    left: 0; right: 0;
    height: 3px;
    background: var(--brand-red);
  }
  .contact .card__rule { top: 88px; }
  .contact__name {
    position: absolute;
    left: 36px; top: 48px;
    font-size: 30px; font-weight: 600;
    letter-spacing: 0.5px;
  }
  .contact__title {
    position: absolute;
    left: 220px; top: 62px;
    font-size: 15px; font-weight: 500;
    letter-spacing: 0.5px;
  }
  .brand-mark {
    position: absolute;
    display: flex; align-items: center; gap: 7px;
    color: var(--brand-red);
    font-weight: 600;
    white-space: nowrap;
  }
  .brand-mark__dot {
    display: block;
    border-radius: 50%;
    background: var(--brand-red);
  }
  .contact .brand-mark { right: 26px; top: 56px; font-size: 16px; letter-spacing: 0.6px; }
  .contact .brand-mark__dot { width: 14px; height: 14px; }

  .details {
    position: absolute;
    left: 36px; top: 114px;
    list-style: none;
    font-size: 13px; font-weight: 500;
  }
  .details li { display: flex; align-items: flex-start; gap: 12px; margin-bottom: 7px; }
  .details li.gap { margin-top: 10px; }
  .details svg { flex: none; width: 15px; height: 15px; margin-top: 1px; }
  .details .address { line-height: 1.55; }
  .icon { fill: none; stroke: var(--brand-red); stroke-width: 1.6; stroke-linecap: round; stroke-linejoin: round; }

  .divider {
    position: absolute;
    left: 300px; top: 124px;
    width: 3px; height: 128px;
    background: var(--brand-red);
  }
  .contact__company {
    position: absolute;
    left: 336px; top: 144px;
    font-size: 40px; font-weight: 600;
    color: var(--brand-red);
    letter-spacing: 0.5px;
  }

  /* Front side */
  .front .card__rule { top: 128px; }
  .front .brand-mark {
    left: 50%; top: 108px;
    transform: translateX(-50%);
    padding: 6px 16px;
    background: var(--card);
    font-size: 26px; letter-spacing: 1px;
  }
  .front .brand-mark__dot { width: 22px; height: 22px; }
  .front__company {
    position: absolute;
    left: 0; right: 0; top: 168px;
    text-align: center;
    font-size: 54px; font-weight: 600;
    color: var(--brand-red);
    letter-spacing: 1px;
  }
  .services {
    position: absolute;
    left: 0; right: 0; top: 252px;
    text-align: center;
    font-size: 16px; font-weight: 500;
    line-height: 1.7;
    letter-spacing: 0.3px;
  }
  .services .sep { margin: 0 8px; }
</style>
</head>
<body>

<section class="card contact" aria-label="Contact side">
  <h1 class="contact__name">OWEN HARTLEY</h1>
  <p class="contact__title">TECHNICAL SALES</p>
  <div class="brand-mark"><span class="brand-mark__dot"></span>CORVANE SHELVING</div>
  <div class="card__rule"></div>

  <ul class="details">
    <li>
      <svg viewBox="0 0 16 16"><path class="icon" d="M8 15s5-5 5-8.5A5 5 0 0 0 3 6.5C3 10 8 15 8 15z"/><circle class="icon" cx="8" cy="6.5" r="1.8"/></svg>
      <span class="address">Nine Ash Close<br>Harrow Mill Business Park<br>Wexley, Derbyshire DE9 4QT</span>
    </li>
    <li class="gap">
      <svg viewBox="0 0 16 16"><rect class="icon" x="4" y="1.5" width="8" height="13" rx="1.5"/><path class="icon" d="M7 12.2h2"/></svg>
      <span>07700 900412</span>
    </li>
    <li>
      <svg viewBox="0 0 16 16"><path class="icon" d="M3 2h3l1.5 3.5-2 1.3a8 8 0 0 0 3.7 3.7l1.3-2L14 10v3a1.5 1.5 0 0 1-1.5 1.5A11.5 11.5 0 0 1 1.5 3.5 1.5 1.5 0 0 1 3 2z"/></svg>
      <span>01632 960581</span>
    </li>
    <li>
      <svg viewBox="0 0 16 16"><rect class="icon" x="1.5" y="6" width="13" height="7" rx="1"/><path class="icon" d="M4.5 6V2h7v4M4.5 10.5h7"/></svg>
      <span>01632 960584</span>
    </li>
    <li class="gap">
      <svg viewBox="0 0 16 16"><rect class="icon" x="1.5" y="3.5" width="13" height="9" rx="1"/><path class="icon" d="M1.5 4l6.5 5 6.5-5"/></svg>
      <span>owen@corvane-shelving.co.uk</span>
    </li>
    <li>
      <svg viewBox="0 0 16 16"><circle class="icon" cx="8" cy="8" r="6.5"/><path class="icon" d="M1.5 8h13M8 1.5c2.2 2 2.2 11 0 13M8 1.5c-2.2 2-2.2 11 0 13"/></svg>
      <span>www.corvane-shelving.co.uk</span>
    </li>
  </ul>

  <div class="divider"></div>
  <p class="contact__company">CORVANE</p>
</section>

<section class="card front" aria-label="Front side">
  <div class="card__rule"></div>
  <div class="brand-mark"><span class="brand-mark__dot"></span>CORVANE SHELVING</div>
  <p class="front__company">CORVANE</p>
  <p class="services">
    MEZZANINE FLOORS<span class="sep">|</span>CANTILEVER RACKING<span class="sep">|</span>PALLET RACKING<span class="sep">|</span>SAFETY BARRIERS<br>
    LONGSPAN SHELVING<span class="sep">|</span>STEEL SHELVING<span class="sep">|</span>PARTITIONING<span class="sep">|</span>TURNKEY PROJECTS
  </p>
</section>

</body>
</html>
```